Business Card Design Harbor of Calm

mental health provider
contemporary
warmth
inviting

Target Market(s)

mental health clients adults

Industry/Entity Type

Mental Health

Contact Information for Business Card

Danielle Korrish PMHNP
2938 SW Fennick Ave
Suite 340C
Portland OR 97225
Fax 503-418-9152
Tel 503-418-9267
Email danielle@dkorrish.com
Website dkorrish.com

Requirements
Nice to have
• see above
Should not have
• no medical logos

```html
<!DOCTYPE html>
<html lang="en">
<head>
<meta charset="utf-8">
<title>Danielle Korrish PMHNP – Business Card</title>
<link rel="stylesheet" href="https://fonts.googleapis.com/css2?family=Arimo:wght@400;700&display=swap">
<style>
  :root {
    --slate: #6d8591;
    --slate-soft: #7a919c;
    --ivory: #f4f6f7;
    --ink: #555a5e;
    --rule: #8a8f93;
    --frame: #c9cdd0;
    --page: #ffffff;
  }
  * { margin: 0; padding: 0; box-sizing: border-box; }
  html, body {
    width: 1200px; height: 381px; overflow: hidden;
    background: var(--page);
    font-family: "Arimo", Arial, sans-serif;
  }
  .sheet { position: relative; width: 1200px; height: 381px; }

  .card-front {
    position: absolute; left: 2px; top: 20px;
    width: 588px; height: 345px;
    background: var(--slate);
    overflow: hidden;
  }
  .ornament-area {
    position: absolute; left: 40px; top: 30px;
    width: 300px; height: 300px;
    border-radius: 50%;
    background: radial-gradient(circle at 50% 50%, var(--slate-soft) 0%, var(--slate-soft) 45%, var(--slate) 72%);
  }
  .provider-name {
    position: absolute; left: 162px; top: 186px;
    color: var(--ivory);
    font-size: 26px; font-weight: 400;
    line-height: 30px;
    letter-spacing: 0.2px;
    white-space: nowrap;
  }

  .card-back {
    position: absolute; left: 609px; top: 20px;
    width: 581px; height: 345px;
    background: var(--page);
    border: 1.5px solid var(--frame);
  }
  .contact-list {
    position: absolute; left: 32px; top: 58px;
    list-style: none;
    color: var(--ink);
    font-size: 27px; line-height: 37px;
  }
  .contact-list .label { font-weight: 700; }
  .contact-list .ruled {
    display: inline-block;
    width: 376px;
    border-bottom: 2px solid var(--rule);
    line-height: 33px;
  }
</style>
</head>
<body>
<main class="sheet">
  <section class="card-front" aria-label="Card front">
    <div class="ornament-area" role="img" aria-label="Decorative open ring with swirling flourish ornament"></div>
    <h1 class="provider-name">Danielle Korrish PMHNP</h1>
  </section>

  <section class="card-back" aria-label="Card back">
    <ul class="contact-list">
      <li>2938 SW Fennick Ave Suite 340C</li>
      <li><span class="ruled">Portland OR 97225</span></li>
      <li><span class="label">Fax</span> 503-418-9152</li>
      <li><span class="ruled"><span class="label">Tel</span> 503-418-9267</span></li>
      <li><span class="label">Email</span> danielle@dkorrish.com</li>
      <li><span class="label">Website</span> www.dkorrish.com</li>
    </ul>
  </section>
</main>
</body>
</html>
```